GLOW AT NINE (EP) FOR KEMURO, AN ARTISTE SIGNED TO HARBOUR MELODIES

A CREATIVELY SIMPLE EVERGREEN DESIGN. BECAUSE NO PICTURE IS REQUIRED, THE DESIGN HAS TO BE VERY EYE CATCHING AND COLOURFUL AND I WANT THE BEST CONCEPT TO DESCRIBE THE TITLE.

DETAILS TO BE USED ON THE DESIGN AS FOLLOWS

RECORDING LABEL: HARBOUR MELODIES
ARTISTE NAME: KEMURO
EP TITLE: GLOW AT NINE
TRACK LIST
1. ENI BABAWO (Produced by Kunle)
2. GROOVE PARADE (Produced by K.O.R Sounds)
3. E DON SWEET (PRODUCED BY B'KEYS)
4. IF THE RAIN COMES TONIGHT SO (PRODUCED BY SLIMMY JAY)
5. RISE SHINE GLOW (PRODUCED BY MIXXA)

ALL SONGS MIXED BY BAYO KNOBS.

Target Market(s)

AFRICA

Font styles to use
Serif
Sans Serif
Decorative
Script

Colors

Designer to choose colors to be used in the design.

Requirements
Must have
• A CREATIVELY SIMPLE EVERGREEN DESIGN
Nice to have
Should not have
• NON

```html
<!DOCTYPE html>
<html lang="en">
<head>
<meta charset="utf-8">
<title>Kemuro – Glow at Nine EP</title>
<link rel="stylesheet" href="https://fonts.googleapis.com/css2?family=Oswald:wght@400;500;600&family=Montserrat:wght@700&display=swap">
<style>
  :root {
    --night: #05050a;
    --night-blue: #16183a;
    --glow-pink: #f07a86;
    --glow-magenta: #d4237a;
    --band-pink: #f6c3c3;
    --band-fade: #ffffff;
    --ink: #0b0b0b;
    --paper: #ffffff;
    --label-orange: #f29a12;
  }
  html, body {
    margin: 0;
    padding: 0;
    width: 1200px;
    height: 1200px;
    overflow: hidden;
    background: var(--paper);
  }
  .cover { display: block; width: 1200px; height: 1200px; }
  .headline { font-family: "Oswald", sans-serif; font-weight: 500; }
  .artist-name { fill: var(--paper); }
  .ep-title { fill: var(--ink); }
  .ep-tag-box { fill: var(--glow-pink); }
  .ep-tag-text { font-family: "Montserrat", sans-serif; font-weight: 700; fill: var(--ink); }
  .credit { font-family: "Oswald", sans-serif; font-weight: 500; fill: var(--ink); }
  .label-name { font-family: "Oswald", sans-serif; font-weight: 400; fill: var(--paper); }
  .label-dot { fill: var(--label-orange); }
</style>
</head>
<body>
<svg class="cover" viewBox="0 0 1200 1200" xmlns="http://www.w3.org/2000/svg">
  <defs>
    <radialGradient id="artGlow" cx="0.45" cy="0.55" r="0.75">
      <stop offset="0" stop-color="var(--glow-magenta)" stop-opacity="0.55"/>
      <stop offset="0.45" stop-color="var(--night-blue)"/>
      <stop offset="1" stop-color="var(--night)"/>
    </radialGradient>
    <linearGradient id="bandFade" x1="0" y1="0" x2="0" y2="1">
      <stop offset="0" stop-color="var(--band-pink)"/>
      <stop offset="1" stop-color="var(--band-fade)"/>
    </linearGradient>
  </defs>

  <rect class="cover-art" x="0" y="0" width="1200" height="904" fill="url(#artGlow)"
        role="img" aria-label="Abstract glowing pink light trails swirling over a spinning vinyl record on a dark background"/>

  <rect class="credit-band" x="0" y="904" width="1200" height="296" fill="url(#bandFade)"/>

  <g class="record-label">
    <circle class="label-dot" cx="1116" cy="162" r="50"/>
    <text class="label-name" x="1112" y="266" font-size="17" text-anchor="middle">HARBOUR MELODIES</text>
  </g>

  <text class="headline artist-name" x="564" y="824" font-size="272"
        textLength="600" lengthAdjust="spacingAndGlyphs">KEMURO</text>

  <rect class="ep-tag-box" x="0" y="798" width="256" height="54"/>
  <text class="ep-tag-text" x="68" y="840" font-size="38"
        textLength="176" lengthAdjust="spacingAndGlyphs">THE EP</text>

  <text class="headline ep-title" x="566" y="1110" font-size="150"
        textLength="592" lengthAdjust="spacingAndGlyphs">GLOW AT NINE</text>

  <g class="producer-credits">
    <text class="credit" x="74" y="974" font-size="50"
          textLength="182" lengthAdjust="spacingAndGlyphs">K.O.R Sounds</text>
    <text class="credit" x="130" y="1040" font-size="72"
          textLength="126" lengthAdjust="spacingAndGlyphs">Kunle</text>
    <text class="credit" x="132" y="1084" font-size="42"
          textLength="116" lengthAdjust="spacingAndGlyphs">B'KEYS</text>
    <text class="credit" x="126" y="1130" font-size="42"
          textLength="132" lengthAdjust="spacingAndGlyphs">SLIMMY JAY</text>
    <text class="credit" transform="translate(74 992) rotate(90)" x="0" y="0" font-size="60"
          textLength="136" lengthAdjust="spacingAndGlyphs">MIXXA</text>
  </g>
</svg>
</body>
</html>
```